Book Cover Contest: "Roads Toward Quiet Grace"

The KR Verlag Islamic Library invites designers and artists to design a cover for the upcoming book “Roads Toward Quiet Grace”.

This inspiring work is by Shaikh Yūsuf al-Karīm ibn Hāmid ibn Ubaydillah al-Mazrūʿī (d. 1376 AH/1957 CE), a renowned Islamic scholar. In his writing, he imparts timeless principles for inner peace and true happiness based on Islamic faith and spiritual knowledge.

Important details for the cover design:
The cover should reflect the theme of the book: paths to happiness, spiritual satisfaction, a fulfilled life.
It may contain both modern and traditional elements, but should be clear, appealing and reader-friendly.
The title “Roads toward quiet grace” should be clearly visible.
Author: Šaiḫ Yūsuf al-Karīm ibn Ḥāmid ibn ʿUbaydillah al-Mazrūʿī
Translation: Marlene Kürten

KR Verlag Islamic Library

Do you have a creative idea for the cover? Then join in and design the face of this inspiring work!

Target Market(s)

Islamic

Font styles to use
Decorative
Script

Requirements
Should not have
• No mosque silhouette, no hanging lamp,

```html
<!DOCTYPE html>
<html lang="en">
<head>
<meta charset="utf-8">
<title>Roads Toward Quiet Grace — Cover</title>
<link rel="stylesheet" href="https://fonts.googleapis.com/css2?family=Parisienne&family=Yellowtail&family=Kaushan+Script&family=Cormorant+SC:wght@600;700&display=swap">
<style>
  :root {
    --paper: #ffffff;
    --maroon: #5a080c;
    --maroon-deep: #43060a;
    --green: #0b5a26;
    --green-deep: #07421b;
    --gold: #e2bd6a;
    --gold-light: #fbe28c;
    --gold-dark: #9c6a1f;
    --ink: #141414;
    --white: #ffffff;
  }
  * { margin: 0; padding: 0; box-sizing: border-box; }
  html, body {
    width: 1137px; height: 1200px; overflow: hidden;
    background: var(--paper);
  }
  .canvas { position: relative; width: 1137px; height: 1200px; }
  .cover-art { position: absolute; left: 0; top: 0; }

  .title { font-weight: 400; font-synthesis: none; }
  .title-lead {
    position: absolute; left: 253px; width: 631px; top: 352px;
    text-align: center; white-space: nowrap;
    font-family: "Parisienne", "Kaushan Script", cursive;
    font-weight: 400;
    font-size: 76px; line-height: 1;
    color: var(--white);
  }
  .title-main {
    position: absolute; left: 253px; width: 631px; top: 470px;
    text-align: center; white-space: nowrap;
    font-family: "Yellowtail", "Kaushan Script", cursive;
    font-weight: 400;
    font-size: 124px; line-height: 1.15;
    background: linear-gradient(100deg, var(--gold-dark) 0%, var(--gold-light) 30%, var(--gold) 55%, var(--gold-dark) 80%, var(--gold-light) 100%);
    -webkit-background-clip: text; background-clip: text;
    color: transparent;
  }
  .rule {
    position: absolute; left: 404px; width: 349px; height: 2px;
    background: linear-gradient(90deg, transparent, var(--gold) 20%, var(--gold-light) 50%, var(--gold) 80%, transparent);
  }
  .rule-top { top: 740px; }
  .rule-bottom { top: 830px; }
  .author {
    position: absolute; left: 253px; width: 631px; top: 756px;
    text-align: center;
    font-family: "Cormorant SC", serif; font-weight: 700;
    font-size: 24px; line-height: 29px;
    color: var(--white);
  }
  .translator {
    position: absolute; left: 253px; width: 631px; top: 868px;
    text-align: center;
    font-family: "Cormorant SC", serif; font-weight: 700;
    font-size: 15px; letter-spacing: 0.5px;
    color: var(--white);
  }
</style>
</head>
<body>
<main class="canvas">
  <svg class="cover-art" width="1137" height="1200" viewBox="0 0 1137 1200" xmlns="http://www.w3.org/2000/svg">
    <defs>
      <linearGradient id="spandrel-tone" x1="0" y1="0" x2="1" y2="1">
        <stop offset="0" stop-color="#0b5a26"/>
        <stop offset="0.5" stop-color="#5d5a2c"/>
        <stop offset="1" stop-color="#0b5a26"/>
      </linearGradient>
    </defs>
    <rect class="board" x="189" y="32" width="758" height="1149" fill="var(--maroon)"/>
    <rect x="210" y="54" width="716" height="1106" fill="none" stroke="var(--gold)" stroke-width="2"/>
    <rect x="216" y="60" width="704" height="1094" fill="none" stroke="var(--ink)" stroke-width="5"/>
    <rect x="224" y="68" width="688" height="1078" fill="none" stroke="var(--gold)" stroke-width="2"/>

    <rect x="232" y="73" width="673" height="106" fill="var(--green)" stroke="var(--gold)" stroke-width="2" role="img" aria-label="Ornamental band with gold medallions"/>
    <rect x="232" y="1034" width="673" height="104" fill="var(--green)" stroke="var(--gold)" stroke-width="2" role="img" aria-label="Ornamental band with gold medallions"/>

    <path d="M232 184 H905 V340 Q860 300 790 292 Q760 232 568 232 Q376 232 346 292 Q276 300 232 340 Z"
          fill="url(#spandrel-tone)" opacity="0.9" role="img" aria-label="Arabesque scroll ornament in the upper corners"/>
    <path d="M232 350 Q285 300 348 300 Q380 244 568 244 Q756 244 788 300 Q851 300 905 350"
          fill="none" stroke="var(--green)" stroke-width="16"/>
    <path d="M232 362 Q288 312 354 310 Q390 258 568 258 Q746 258 782 310 Q848 312 905 362"
          fill="none" stroke="var(--gold)" stroke-width="2"/>

    <path d="M232 1030 H905 V876 Q860 916 790 924 Q760 984 568 984 Q376 984 346 924 Q276 916 232 876 Z"
          fill="url(#spandrel-tone)" opacity="0.9" role="img" aria-label="Arabesque scroll ornament in the lower corners"/>
    <path d="M232 866 Q285 916 348 916 Q380 972 568 972 Q756 972 788 916 Q851 916 905 866"
          fill="none" stroke="var(--green)" stroke-width="16"/>
    <path d="M232 854 Q288 904 354 906 Q390 958 568 958 Q746 958 782 906 Q848 904 905 854"
          fill="none" stroke="var(--gold)" stroke-width="2"/>
  </svg>

  <h1 class="title">
    <span class="title-lead">Roads Toward</span>
    <span class="title-main">Quiet Grace</span>
  </h1>

  <div class="rule rule-top"></div>
  <p class="author">Šaiḫ Yūsuf al-Karīm<br>ibn Ḥāmid ibn ʿUbaydillah al-Mazrūʿī</p>
  <div class="rule rule-bottom"></div>
  <p class="translator">Translation: Marlene Kürten</p>
</main>
</body>
</html>
```